Marcus Lindqvist Photography needs a business card designs

I am looking for a business card with a logo clean and simple which I can use that logo on my website or on my pictures. It has to be very classy and very professional. Please look at my website at www.marcuslvqphoto.com for my signature. I'm thinking of something like that for my signature/logo. I'm still working on my website but you get an idea. I'm open to any design but not too busy graphics.

I will be printing the business card from qrivel.com.

Surprise me :)

contact me if you have any questions.

-ML

I'm receiving a lot of black background at the moment. I know my website is all black doesn't mean I want my card to be all black. Please send in with some white background as well. Thanks :)

check out some business cards that I found online. I think they are simple and look really awesome. I don't want a card that is too busy.

http://www.marcuslvqphoto.com/p270092084

Reason: Please extend the date for me. I haven't really receive any good design yet.

Printing

• -a logo that related to my first and last initial of my name "ML"
-double sided
• -I don't want my background to be all black.
-no pictures on the card

```html
<!DOCTYPE html>
<html lang="en">
<head>
<meta charset="utf-8">
<title>Marcus Lindqvist Photography — Business Cards</title>
<link rel="stylesheet" href="https://fonts.googleapis.com/css2?family=Jost:wght@400;500&display=swap">
<style>
  :root {
    --page: #ffffff;
    --card-light-top: #ffffff;
    --card-light-bottom: #e9e9e9;
    --card-dark: #050505;
    --ink: #1a1a1a;
    --accent: #e8233f;
    --mono-white: #ffffff;
    --mark-fill: #1c1c1c;
    --band-top: #4a4a4a;
    --band-bottom: #050505;
  }
  html, body {
    margin: 0;
    padding: 0;
    width: 1200px;
    height: 800px;
    overflow: hidden;
    background: var(--page);
  }
  .sheet {
    position: relative;
    width: 1200px;
    height: 800px;
    font-family: "Jost", "Futura", sans-serif;
  }
  .card {
    position: absolute;
    width: 217px;
    height: 334px;
    overflow: hidden;
    box-shadow: 0 2px 6px rgba(0,0,0,0.22);
  }
  .card--rounded { border-radius: 16px; }

  .card--front {
    background: radial-gradient(ellipse at 40% 30%, var(--card-light-top) 0%, var(--card-light-top) 35%, var(--card-light-bottom) 100%);
    color: var(--ink);
  }
  .card--back { background: var(--card-dark); }

  .set-square .card--front { left: 40px; top: 114px; }
  .set-square .card--back  { left: 305px; top: 114px; }
  .set-rounded .card--front { left: 669px; top: 354px; }
  .set-rounded .card--back  { left: 934px; top: 354px; }

  .monogram {
    position: absolute;
    border-radius: 50%;
    background: var(--mark-fill);
    display: flex;
    align-items: center;
    justify-content: center;
    color: var(--accent);
    font-weight: 500;
    line-height: 1;
  }
  .card--front .monogram {
    left: 126px; top: 14px;
    width: 80px; height: 80px;
    font-size: 34px;
  }
  .card--back .monogram {
    left: 39px; top: 66px;
    width: 138px; height: 138px;
    font-size: 58px;
  }

  .holder {
    position: absolute;
    left: 9px;
    top: 146px;
  }
  .holder__name {
    margin: 0;
    font-size: 26px;
    font-weight: 400;
    color: var(--accent);
    line-height: 1;
    letter-spacing: -0.2px;
    white-space: nowrap;
  }
  .holder__role {
    margin: 3px 0 0 2px;
    font-size: 11.5px;
    letter-spacing: 3.6px;
    color: var(--ink);
    line-height: 1;
  }

  .contact {
    position: absolute;
    left: 11px;
    top: 220px;
    margin: 0;
    font-size: 10px;
    line-height: 15px;
  }
  .contact__row { display: flex; }
  .contact__label {
    width: 40px;
    color: var(--accent);
  }
  .contact__value { color: var(--ink); }

  .web-band {
    position: absolute;
    left: 0; right: 0; bottom: 0;
    height: 39px;
    background: linear-gradient(180deg, var(--band-top) 0%, var(--band-bottom) 55%);
    color: var(--mono-white);
    font-size: 16.5px;
    letter-spacing: 0.4px;
    display: flex;
    align-items: center;
    justify-content: center;
  }

  .studio-name {
    position: absolute;
    left: 0; right: 0;
    top: 222px;
    text-align: center;
    color: var(--mono-white);
    font-weight: 400;
    line-height: 1.1;
  }
  .studio-name__person {
    display: block;
    font-size: 23px;
  }
  .studio-name__trade {
    display: block;
    font-size: 13px;
    letter-spacing: 5px;
    margin-top: 2px;
  }
</style>
</head>
<body>
<main class="sheet">

  <section class="card-set set-square">
    <article class="card card--front">
      <div class="monogram">ML</div>
      <div class="holder">
        <h1 class="holder__name">Marcus Lindqvist</h1>
        <p class="holder__role">PHOTOGRAPHER</p>
      </div>
      <dl class="contact">
        <div class="contact__row"><dt class="contact__label">Phone:</dt><dd class="contact__value" style="margin:0">987-65432</dd></div>
        <div class="contact__row"><dt class="contact__label">E-mail:</dt><dd class="contact__value" style="margin:0">info@marcuslvqphoto.com</dd></div>
      </dl>
      <div class="web-band">www.marcuslvqphoto.com</div>
    </article>
    <article class="card card--back">
      <div class="monogram">ML</div>
      <p class="studio-name">
        <span class="studio-name__person">Marcus Lindqvist</span>
        <span class="studio-name__trade">PHOTOGRAPHY</span>
      </p>
    </article>
  </section>

  <section class="card-set set-rounded">
    <article class="card card--front card--rounded">
      <div class="monogram">ML</div>
      <div class="holder">
        <h1 class="holder__name">Marcus Lindqvist</h1>
        <p class="holder__role">PHOTOGRAPHER</p>
      </div>
      <dl class="contact">
        <div class="contact__row"><dt class="contact__label">Phone:</dt><dd class="contact__value" style="margin:0">987-65432</dd></div>
        <div class="contact__row"><dt class="contact__label">E-mail:</dt><dd class="contact__value" style="margin:0">info@marcuslvqphoto.com</dd></div>
      </dl>
      <div class="web-band">www.marcuslvqphoto.com</div>
    </article>
    <article class="card card--back card--rounded">
      <div class="monogram">ML</div>
      <p class="studio-name">
        <span class="studio-name__person">Marcus Lindqvist</span>
        <span class="studio-name__trade">PHOTOGRAPHY</span>
      </p>
    </article>
  </section>

</main>
</body>
</html>
```